Business cards and stationary for Mortgage Company
Brightwell Lending Partners Inc.
Professional
Peter K Ostrand
Licensed Mortgage Originator
47 Alder Brook Lane
Newtown, Pa 18977
1-855-314-HOME (4663)
peterkostrand@brightwelllendingpartners.example
www.brightwelllendingpartners.example
NMLS# 417205 and NMLS #418362
Looking for stationary and business cards to use logo with black letters on white background, and examples using white letters on black ground . Red graphic is the same on either choice.
Just the logo in either black on white, or white on black background.

```html
<!DOCTYPE html>
<html lang="en">
<head>
<meta charset="utf-8">
<title>Brightwell Lending Partners – Stationery Set</title>
<link rel="stylesheet" href="https://fonts.googleapis.com/css2?family=Tinos:wght@400;700&family=Arimo:wght@400;700&display=swap">
<style>
  :root {
    --stage: #6f6f6f;
    --stage-dark: #5d5d5d;
    --paper: #ffffff;
    --ink: #1a1a1a;
    --muted: #8a8a8a;
    --brand-red: #e41e26;
    --brand-black: #111111;
    --faint-red: #fbe5e2;
    --label: #d9d9d9;
    --rule: #bbbbbb;
  }
  * { box-sizing: border-box; margin: 0; padding: 0; }
  html, body { width: 1200px; height: 461px; overflow: hidden; }
  body {
    background: linear-gradient(90deg, var(--stage-dark), var(--stage) 40%, var(--stage-dark));
    font-family: "Arimo", Arial, sans-serif;
    color: var(--ink);
    position: relative;
  }
  .item { position: absolute; }
  .item-label {
    position: absolute; top: -8px; left: 0; right: 0;
    text-align: center; font-size: 5px; color: var(--label); letter-spacing: .2px; white-space: nowrap;
  }
  .sheet { background: var(--paper); box-shadow: 0 1px 3px rgba(0,0,0,.35); }

  /* brand lockup */
  .brand { display: inline-flex; align-items: center; gap: 3px; font-family: "Tinos", "Times New Roman", serif; font-weight: 700; white-space: nowrap; color: var(--ink); }
  .brand-mark { display: inline-block; background: var(--brand-red); flex: none; }
  .brand--light { color: var(--paper); }

  /* business cards */
  .card { width: 89px; height: 50px; display: flex; align-items: center; justify-content: center; overflow: hidden; }
  .card .brand { font-size: 6px; }
  .card .brand-mark { width: 5px; height: 5px; }
  .card--red { background: var(--brand-red); }
  .card--red .brand-mark { background: var(--paper); }
  .card--black { background: var(--brand-black); }
  .card-back { flex-direction: column; align-items: flex-start; justify-content: space-between; padding: 6px 7px; }
  .card-back .brand { font-size: 5px; }
  .card-back .brand-mark { width: 4px; height: 4px; }
  .card-back .contact { font-size: 3.2px; line-height: 4.4px; white-space: nowrap; }
  .card-back .person { font-size: 4.5px; font-weight: 700; }
  .card--red .contact, .card--black .contact { color: var(--paper); }

  /* compliment slip */
  .slip { padding: 8px 10px; overflow: hidden; }
  .slip .brand { font-size: 8px; }
  .slip .brand-mark { width: 7px; height: 7px; }
  .slip-contact { position: absolute; right: 10px; top: 9px; font-size: 3.2px; line-height: 4.3px; text-align: right; color: var(--muted); }
  .slip-watermark { position: absolute; right: 14px; bottom: 10px; width: 60px; height: 60px; background: var(--faint-red); }

  /* envelopes */
  .envelope { width: 293px; height: 84px; overflow: hidden; }
  .envelope .brand { position: absolute; font-size: 6px; }
  .envelope .brand-mark { width: 5px; height: 5px; }
  .envelope-front .brand { left: 10px; top: 8px; }
  .envelope-back .brand { left: 50%; top: 66px; transform: translateX(-50%); }
  .envelope-back svg { position: absolute; inset: 0; }
  .envelope--red { background: var(--brand-red); }
  .envelope--red .brand-mark { background: var(--paper); }
  .envelope--black { background: var(--brand-black); }
  .envelope-return { position: absolute; left: 10px; top: 17px; font-size: 3px; line-height: 4px; color: var(--muted); }
  .envelope--red .envelope-return, .envelope--black .envelope-return { color: var(--label); }

  /* letterheads */
  .letterhead { width: 206px; height: 282px; padding: 12px 14px; overflow: hidden; }
  .letterhead .brand { font-size: 8px; }
  .letterhead .brand-mark { width: 7px; height: 7px; }
  .letterhead-address { position: absolute; right: 14px; top: 12px; font-size: 3px; line-height: 4px; text-align: right; color: var(--muted); }
  .letterhead-watermark { position: absolute; left: 40px; top: 100px; width: 125px; height: 125px; background: var(--faint-red); }
  .letterhead-footer { position: absolute; left: 0; right: 0; bottom: 8px; text-align: center; font-size: 3px; color: var(--muted); }

  .fax-title { position: absolute; right: 14px; top: 30px; font-size: 6px; font-weight: 700; color: var(--ink); }
  .fax-table { position: absolute; left: 14px; top: 38px; width: 178px; border-collapse: collapse; font-size: 3.5px; }
  .fax-table td { border: .5px solid #999; height: 8px; padding: 0 2px; }
  .fax-table td.key { width: 22px; font-weight: 700; background: #f1f1f1; }
  .fax-checks { position: absolute; left: 14px; top: 84px; display: flex; gap: 10px; font-size: 3.5px; }
  .fax-checks span::before { content: ""; display: inline-block; width: 3px; height: 3px; border: .5px solid #555; margin-right: 2px; vertical-align: middle; }
</style>
</head>
<body>

<!-- Business cards -->
<div class="item sheet card" style="left:271px;top:24px">
  <span class="item-label">Card Front</span>
  <span class="brand"><span class="brand-mark"></span>Brightwell Lending Partners</span>
</div>
<div class="item sheet card card-back" style="left:374px;top:24px">
  <span class="item-label">Card Back</span>
  <span class="brand"><span class="brand-mark"></span>Brightwell Lending Partners</span>
  <div class="contact"><div class="person">Peter K Ostrand</div>Licensed Mortgage Originator<br>Office phone line here<br>www.brightwelllendingpartners.example</div>
</div>
<div class="item card card--red" style="left:470px;top:24px">
  <span class="item-label">Alternate Front</span>
  <span class="brand brand--light"><span class="brand-mark"></span>Brightwell Lending Partners</span>
</div>
<div class="item card card--red card-back" style="left:571px;top:24px">
  <span class="item-label">Alternate Back</span>
  <span class="brand brand--light"><span class="brand-mark"></span>Brightwell Lending Partners</span>
  <div class="contact"><div class="person">Peter K Ostrand</div>Office street address here<br>Office phone line here<br>peterkostrand@brightwelllendingpartners.example</div>
</div>
<div class="item sheet card" style="left:271px;top:86px">
  <span class="brand"><span class="brand-mark"></span>Brightwell Lending Partners</span>
</div>
<div class="item sheet card card-back" style="left:374px;top:86px">
  <span class="brand"><span class="brand-mark"></span>Brightwell Lending Partners</span>
  <div class="contact"><div class="person">Peter K Ostrand</div>Licensed Mortgage Originator<br>Office phone line here<br>www.brightwelllendingpartners.example</div>
</div>
<div class="item card card--black" style="left:470px;top:86px">
  <span class="brand brand--light"><span class="brand-mark"></span>Brightwell Lending Partners</span>
</div>
<div class="item card card--black card-back" style="left:571px;top:86px">
  <span class="brand brand--light"><span class="brand-mark"></span>Brightwell Lending Partners</span>
  <div class="contact"><div class="person">Peter K Ostrand</div>Office street address here<br>Office phone line here<br>peterkostrand@brightwelllendingpartners.example</div>
</div>

<!-- Compliment slip -->
<div class="item sheet slip" style="left:667px;top:24px;width:221px;height:113px">
  <span class="item-label">Compliment Slip</span>
  <span class="brand"><span class="brand-mark"></span>Brightwell Lending Partners</span>
  <div class="slip-contact">Office street address<br>City, State Zip<br>Office phone line<br>www.brightwelllendingpartners.example</div>
  <div class="slip-watermark" role="img" aria-label="Faint brand symbol decoration"></div>
</div>

<!-- Envelopes -->
<div class="item sheet envelope envelope-front" style="left:900px;top:18px">
  <span class="item-label">Envelopes</span>
  <span class="brand"><span class="brand-mark"></span>Brightwell Lending Partners</span>
  <div class="envelope-return">Office street address<br>City, State Zip</div>
</div>
<div class="item sheet envelope envelope-back" style="left:900px;top:88px">
  <svg width="293" height="84" viewBox="0 0 293 84"><polyline points="0,0 146.5,52 293,0" fill="none" stroke="#bbb" stroke-width="1"/></svg>
  <span class="brand"><span class="brand-mark"></span>Brightwell Lending Partners</span>
</div>
<div class="item envelope envelope-front envelope--red" style="left:900px;top:158px">
  <span class="brand brand--light"><span class="brand-mark"></span>Brightwell Lending Partners</span>
</div>
<div class="item sheet envelope envelope-back" style="left:900px;top:228px">
  <svg width="293" height="84" viewBox="0 0 293 84"><polygon points="0,0 293,0 146.5,52" fill="#e41e26"/></svg>
  <span class="brand"><span class="brand-mark"></span>Brightwell Lending Partners</span>
</div>
<div class="item envelope envelope-front envelope--black" style="left:900px;top:298px">
  <span class="brand brand--light"><span class="brand-mark"></span>Brightwell Lending Partners</span>
</div>
<div class="item sheet envelope envelope-back" style="left:900px;top:366px">
  <svg width="293" height="84" viewBox="0 0 293 84"><polygon points="0,0 293,0 146.5,52" fill="#111"/></svg>
  <span class="brand"><span class="brand-mark"></span>Brightwell Lending Partners</span>
</div>

<!-- Letterheads -->
<div class="item sheet letterhead" style="left:19px;top:163px">
  <span class="item-label">Fax Cover Sheet</span>
  <span class="brand"><span class="brand-mark"></span>Brightwell Lending Partners</span>
  <div class="fax-title">FAX</div>
  <table class="fax-table">
    <tr><td class="key">To</td><td></td><td class="key">From</td><td></td></tr>
    <tr><td class="key">Fax</td><td></td><td class="key">Phone</td><td></td></tr>
    <tr><td class="key">Re</td><td></td><td class="key">Date</td><td></td></tr>
    <tr><td class="key">Pages</td><td></td><td class="key">CC</td><td></td></tr>
  </table>
  <div class="fax-checks"><span>Urgent</span><span>Review</span><span>Reply</span><span>Recycle</span><span>Comment</span></div>
  <div class="letterhead-watermark" style="top:110px" role="img" aria-label="Faint brand symbol decoration"></div>
  <div class="letterhead-footer">Office address · City, State Zip · Phone line · License number</div>
</div>

<div class="item sheet letterhead" style="left:240px;top:163px">
  <span class="item-label">Letterhead</span>
  <span class="brand"><span class="brand-mark"></span>Brightwell Lending Partners</span>
  <div class="letterhead-watermark" role="img" aria-label="Faint brand symbol decoration"></div>
  <div class="letterhead-footer">www.brightwelllendingpartners.example · License number</div>
</div>

<div class="item sheet letterhead" style="left:456px;top:163px">
  <span class="item-label">Fax Cover Alternate</span>
  <span class="brand"><span class="brand-mark"></span>Brightwell Lending Partners</span>
  <div class="fax-title">FAX</div>
  <table class="fax-table">
    <tr><td class="key">To</td><td></td><td class="key">From</td><td></td></tr>
    <tr><td class="key">Fax</td><td></td><td class="key">Phone</td><td></td></tr>
    <tr><td class="key">Re</td><td></td><td class="key">Date</td><td></td></tr>
    <tr><td class="key">Pages</td><td></td><td class="key">CC</td><td></td></tr>
  </table>
  <div class="fax-checks"><span>Urgent</span><span>Review</span><span>Reply</span><span>Recycle</span><span>Comment</span></div>
  <div class="letterhead-watermark" style="top:110px" role="img" aria-label="Faint brand symbol decoration"></div>
  <div class="letterhead-footer">Office address · City, State Zip · Phone line · License number</div>
</div>

<div class="item sheet letterhead" style="left:684px;top:163px">
  <span class="item-label">Letterhead Second</span>
  <span class="brand"><span class="brand-mark"></span>Brightwell Lending Partners</span>
  <div class="letterhead-address">Peter K Ostrand<br>Office street address<br>City, State Zip<br>Office phone line<br>peterkostrand@brightwelllendingpartners.example</div>
  <div class="letterhead-watermark" role="img" aria-label="Faint brand symbol decoration"></div>
  <div class="letterhead-footer">www.brightwelllendingpartners.example · License number</div>
</div>

</body>
</html>
```